Q.R. Bright Desk Store

The design is for eCommerce home page but I would like it to complement this site: http://www.qrbrightdesksystems.com/ but... it should also have independence as a standalone site.

The best design will be able to effectively mix corporate with a high quality small business consumer feel. It should be completely custom design, not a template look or feel. I want the users to get the feeling that this is the place to go for buying tech for business. We sell the same products as Vantrel.

You can be creative as you wish, as long as the elements of a great eCommerce site are present.

I would like your 'design' to blow these away:
http://www.buying.zorvex.com/
mivoland.com
http://www.vantrel.com/

Here are references:
Call to action
http://trabelwise.com/us/blog/48173-seven-tips-for-designing-an-effective-ecommerce-call-to-action

Effective Ecommerce design
http://www.plov.com/ss/7-tips-for-effective-e-commerce#0

91 points of ecommerce
http://dreb.com/blog/holygrail-of-ecommerce-conversion-optimization-91-points-checklist

UPDATE 07/11/2013:

Please look at the category sample png files. I see already many people are using the main menu from qrbrightdesksystems.com and I do not mind your creativiety, but this is an eCommerce store and people need a menu to get to the categories and/or product types. I don't want to limit anyone creativity by the png samples. I'm also not using them to show I like them in any particular way or form, just that it's needed, whether it's a button (dropdown of course) that says 'Categories' or 'Products, whether it an accordion, horizontal or vertical.

Thanks

UPDATE 07/12/2013:

Please find other use of space that has been used for About Us paragraph (if you've added it to the page). About Us should have it's own page and the purpose of the design should be to sell products (and some services as products). Please put a link or some other creative method to lead users to the About Us page.

Reason: I've raised the award, including 1st, 2nd, and 3rd place and participation payments so I will also extend 7 days. Thanks!

I've updated the product brief. Please scroll down to where it says: UPDATE 07/11/2013

Thanks!

UPDATE 07/12/2013:

Please find other use of space that has been used for About Us paragraph (if you've added it to the page).  About Us should have it's own page and the purpose of the design should be to sell products (and some services as products). Please put a link or some other creative method to lead users to the About Us page if you must but not on the real estate of the page.

Thanks!

Added updates to the brief 7/14/2013.

Thanks!

The voting is in and the project is complete.  Thanks everyone for joining, all of those who participated are truly amazingly talented. But, there were only 3 prizes.  I will be having further projects down the line to develop other pages to this site after the initial implementation is completed.  I truly would like to have you all back. 

- Thank you.

Target Market(s)

corporate decision-makers AND small business consumers

Industry/Entity Type

Small Business

Requirements
Must have
• Call to action.
Openness (non-clutter).

These elements:
Search box
Logo
Tagline
Telephone number
Contact details
Address
My account / sign in
Shopping basket / checkout link
Latest offers
Promotional area
Email sign up
Delivery information
About us
Link to press office / corporate site
Terms and conditions
Sitemap for the footer.
Delivery offers: free
Personalized recommendations
Social media links
Accepted payment methods
Link to blog or community section
Change language / country

http://freshnotesblog.kelvarant.com/sales-leads-landing-page/

UPDATE 07/14/2013
Category Menu. This can be a dropdown, horizontal, vertical, etc. But shoppers need to know how to get to the products they want to buy.
Nice to have
• Trustmarks
Blog/Blog link

UPDATE 07/12/2013:
Make the footer useful.

UPDATE 07/14/2013 (Suggestions of elements to differentiate your designs)

-Quick Shop: A quick buy module/section: Where a user can put in a SKU number or Model number to quickly add the product to their shopping cart.

-Featured
-Best Sellers
-Specials
-Trending Tags/Tag Cloud
- Activity Stream
- Cross Sell/ Up Sell
- Testimonial
- Social Network Feed
- Live Help
- Feedback/Support/Contact Tab
- Show logged in user (i.e. Welcome, Mark Pell)
Should not have
• The design SHOULD NOT be generic like this:

http://www.artflock.com/design/52392
http://www.pelicanvault.com/

The page should not feel over cluttered. It should not have low quality icons or design elements. Navigation should not be hard to discover or confusing.

```html
<!DOCTYPE html>
<html lang="en">
<head>
<meta charset="utf-8">
<title>Q.R. Bright Desk Solutions</title>
<link rel="stylesheet" href="https://fonts.googleapis.com/css2?family=Montserrat:wght@300;400;500;600;700;800&family=Crimson+Text:ital@1&display=swap">
<style>
:root{
  --navy:#13306e;
  --blue:#1565b8;
  --sky:#1e9be0;
  --band-top:#1aa0e6;
  --band-bottom:#0a3d8f;
  --green:#5aa31b;
  --green-dark:#3f7d0c;
  --ink:#333;
  --grey:#666;
  --rule:#d8d8d8;
  --footer-text:#9a9a9a;
}
*{margin:0;padding:0;box-sizing:border-box}
html,body{width:1200px;height:1142px;overflow:hidden;background:#fff}
body{position:relative;font-family:Arial,Helvetica,sans-serif;color:var(--ink)}
.abs{position:absolute}
ul{list-style:none}
a{text-decoration:none}

/* top bar */
.topbar{left:0;top:0;width:1200px;height:39px;background:linear-gradient(#2a2a2a,#060606)}
.topnav{left:174px;top:0;display:flex;height:39px}
.topnav a{font-family:Montserrat,sans-serif;font-weight:600;font-size:14.5px;color:#fff;padding:0 9px;line-height:39px}
.topnav a.current{background:#3a3a3a;padding:0 14px}
.utility{left:788px;top:0;display:flex;gap:14px;line-height:39px}
.utility a{font-family:"Crimson Text",serif;font-style:italic;font-size:13px;color:#fff}
.cart{left:970px;top:0;width:65px;height:39px;background:#333;font-family:"Crimson Text",serif;font-style:italic;font-size:13px;color:#fff;display:flex;align-items:center;justify-content:center;gap:6px}

/* hero photo sits behind header pieces */
.hero-photo{left:143px;top:186px;width:914px;height:437px;background:radial-gradient(ellipse at 38% 45%,#3d4656 0,#6b7180 22%,#c9d8c1 48%,#eef2ea 70%,#fff 92%);z-index:0}

/* header */
.brand{left:174px;top:64px;display:flex;align-items:center;gap:12px;z-index:2}
.brand-dot{width:72px;height:72px;border-radius:50%;background:var(--blue)}
.brand-name{font-family:Montserrat,sans-serif;font-weight:500;color:var(--blue);font-size:21px;line-height:1.1;letter-spacing:.3px}
.search{left:511px;top:57px;width:195px;height:23px;border:1px solid #bbb;border-radius:12px;background:#f4f4f4;font-size:9px;color:#555;padding:5px 0 0 16px;z-index:2}
.search svg{position:absolute;right:8px;top:4px}
.help{left:776px;top:57px;font-family:"Crimson Text",serif;font-style:italic;font-size:12px;color:#555;z-index:2}
.phone{display:flex;align-items:center;gap:6px;font-family:Montserrat,sans-serif;font-weight:600}
.head-phone{left:892px;top:52px;font-size:21px;color:var(--navy);z-index:2}
.service{top:94px;display:block;font-family:Montserrat,sans-serif;font-size:15px;line-height:22px;color:var(--blue);z-index:2}
.service span{font-weight:400}
.service b{font-weight:700}
.service-rule{top:98px;height:42px;border-left:1px dotted #9ab;z-index:2}

/* category menu */
.catbar{left:171px;top:157px;width:857px;height:29px;border:1px solid #ccc;background:linear-gradient(#fff,#ececec);display:flex;z-index:3}
.catbar a{font-family:Montserrat,sans-serif;font-size:11px;color:#333;padding:0 12px;line-height:27px;border-right:1px solid #ccc;display:flex;align-items:center;gap:4px}
.catbar a::after{content:"";border:4px solid transparent;border-top:5px solid #999;margin-top:5px}
.catbar a.open::after{border-top-color:#222}

/* hero copy */
.hero-copy{left:744px;top:345px;font-family:Montserrat,sans-serif;color:var(--navy);font-weight:800;line-height:1;z-index:2}
.hero-copy .l1{font-size:19px;font-weight:700}
.hero-copy .l2{font-size:38px;margin-top:6px}
.hero-copy .l3{font-size:27px}
.cta{left:745px;top:462px;width:258px;height:54px;background:linear-gradient(var(--green),var(--green-dark));border:1px solid #2f6408;display:flex;align-items:center;gap:12px;padding-left:16px;font-family:Montserrat,sans-serif;font-weight:600;font-size:18px;color:#fff;z-index:2}

/* blue band */
.band{left:0;top:623px;width:1200px;height:117px;background:linear-gradient(var(--band-top),var(--band-bottom))}
.feature{top:654px;height:56px;display:flex;align-items:center;gap:14px;font-family:Montserrat,sans-serif;font-size:16px;color:#fff;line-height:22px}
.feature span{font-weight:300;display:block}
.feature b{font-weight:700;display:block}

/* panels */
.panel{top:748px;height:125px;background:linear-gradient(#f1f1f1,#fff 40%);box-shadow:0 1px 3px rgba(0,0,0,.2);padding:16px 0 0 30px}
.panel h2{font-family:Montserrat,sans-serif;font-size:19px;color:var(--navy);font-weight:400;letter-spacing:.3px}
.panel h2 b{font-weight:700}
.cols{display:flex;margin-top:10px}
.cols ul li{font-size:10.5px;color:#444;line-height:16px}
.cols ul li::before{content:"• "}

/* footer */
.footer{left:0;top:913px;width:1200px;height:185px;background:linear-gradient(#222,#000)}
.foot-h{top:940px;font-family:Montserrat,sans-serif;font-size:16px;color:#fff;font-weight:400}
.foot-list{top:983px}
.foot-list li{font-size:10.5px;color:var(--footer-text);line-height:16px}
.foot-phone{left:831px;top:960px;font-size:26px;color:#fff}
.foot-brand{left:870px;top:1002px;display:flex;align-items:center;gap:8px}
.foot-brand .dot{width:72px;height:72px;border-radius:50%;background:var(--blue)}
.foot-brand span{font-family:Montserrat,sans-serif;font-weight:500;font-size:12px;color:#fff;width:80px;line-height:1.2}
.bottom{left:0;top:1098px;width:1200px;height:44px;background:#151515;border-top:1px solid #333}
.legal{left:203px;top:1109px;display:flex;gap:12px;font-size:10.5px;color:var(--footer-text)}
.social{left:582px;top:1106px;display:flex;gap:8px}
.social i{display:block;width:15px;height:15px;border-radius:50%;background:#fff}
.copy{right:166px;top:1109px;font-size:10.5px;color:var(--footer-text)}
</style>
</head>
<body>

<div class="abs topbar"></div>
<nav class="abs topnav">
  <a class="current" href="#">HOME</a><a href="#">SMALL BUSINESS</a><a href="#">ENTERPRISE</a><a href="#">NON-PROFIT</a>
</nav>
<div class="abs utility"><a href="#">Log In</a><a href="#">Sign Up</a><a href="#">Help</a><a href="#">Contact</a></div>
<div class="abs cart">
  <svg width="12" height="10" viewBox="0 0 12 10"><path d="M0 1h2l2 6h6l2-5H3" fill="none" stroke="#fff" stroke-width="1.4"/><circle cx="5" cy="9" r="1" fill="#fff"/><circle cx="9" cy="9" r="1" fill="#fff"/></svg>Cart
</div>

<div class="abs hero-photo" role="img" aria-label="Photo of a smiling businessman in a suit at a laptop in a bright office, colleagues blurred behind"></div>

<header>
  <div class="abs brand">
    <div class="brand-dot"></div>
    <div class="brand-name">Q.R. BRIGHT DESK<br>SOLUTIONS</div>
  </div>
  <div class="abs search">ENTER KEYWORD
    <svg width="14" height="14" viewBox="0 0 14 14"><circle cx="5.5" cy="5.5" r="4.2" fill="none" stroke="#555" stroke-width="1.8"/><path d="M8.6 8.6l4 4" stroke="#555" stroke-width="2"/></svg>
  </div>
  <div class="abs help">We're Here to Help!</div>
  <div class="abs phone head-phone">
    <svg width="16" height="16" viewBox="0 0 16 16"><path d="M3 1l3 3-2 2c1 2 3 4 5 5l2-2 3 3-2 3C7 14 2 9 1 3z" fill="var(--blue)"/></svg>888.555.0142
  </div>
  <nav>
    <a class="abs service" style="left:514px" href="#"><span>HARDWARE</span><br><b>FULFILLMENT</b></a>
    <div class="abs service-rule" style="left:634px"></div>
    <a class="abs service" style="left:651px" href="#"><span>SOFTWARE</span><br><b>LICENSING</b></a>
    <div class="abs service-rule" style="left:759px"></div>
    <a class="abs service" style="left:777px" href="#"><span>IT RESOURCE</span><br><b>MANAGEMENT</b></a>
    <div class="abs service-rule" style="left:905px"></div>
    <a class="abs service" style="left:921px" href="#"><span>TECHNOLOGY</span><br><b>SERVICES</b></a>
  </nav>
  <nav class="abs catbar">
    <a class="open" href="#">PRODUCTS</a><a href="#">SOLUTIONS</a><a href="#">MARKETS</a><a href="#">TOOLS</a><a href="#">SERVICES</a><a href="#" style="padding:0 18px 0 12px">MANUFACTURER STORES</a>
  </nav>
</header>

<section>
  <h1 class="abs hero-copy"><div class="l1">YOUR COMPLETE</div><div class="l2">IT RESOURCE</div><div class="l3">MANAGMENT</div></h1>
  <a class="abs cta" href="#">
    <svg width="40" height="40" viewBox="0 0 40 40"><circle cx="20" cy="20" r="17" fill="none" stroke="#fff" stroke-width="2"/><path d="M8 26q2 8 10 8" fill="none" stroke="#fff" stroke-width="2"/></svg>REQUEST A QUOTE
  </a>
</section>

<section>
  <div class="abs band"></div>
  <div class="abs feature" style="left:206px">
    <svg width="42" height="42" viewBox="0 0 42 42"><circle cx="14" cy="14" r="9" fill="none" stroke="#fff" stroke-width="6"/><path d="M20 20l16 16" stroke="#fff" stroke-width="7" stroke-linecap="round"/><circle cx="32" cy="10" r="5" fill="#fff"/><path d="M6 36l10-10" stroke="#fff" stroke-width="5" stroke-linecap="round"/></svg>
    <div><span>HARDWARE</span><b>FULFILLMENT</b></div>
  </div>
  <div class="abs feature" style="left:412px">
    <svg width="52" height="52" viewBox="0 0 54 54"><circle cx="27" cy="27" r="26" fill="#fff"/><circle cx="27" cy="27" r="9" fill="none" stroke="var(--blue)" stroke-width="2.5"/><circle cx="27" cy="27" r="3" fill="var(--blue)"/></svg>
    <div><span>SOFTWARE</span><b>LICENSING</b></div>
  </div>
  <div class="abs feature" style="left:605px">
    <svg width="50" height="50" viewBox="0 0 52 52"><ellipse cx="26" cy="15" rx="10" ry="12" fill="#fff"/><path d="M2 52q2-20 24-22q22 2 24 22z" fill="#fff"/></svg>
    <div><span>IT RESOURCE</span><b>MANAGEMENT</b></div>
  </div>
  <div class="abs feature" style="left:834px">
    <svg width="56" height="42" viewBox="0 0 56 42"><rect x="8" y="2" width="40" height="30" fill="none" stroke="#fff" stroke-width="2.5"/><path d="M2 36h52l-3 4H5z" fill="#fff"/></svg>
    <div><span>TECHNOLOGY</span><b>SERVICES</b></div>
  </div>
</section>

<section>
  <div class="abs panel" style="left:175px;width:420px">
    <h2><b>VERTICAL</b> MARKETS</h2>
    <div class="cols">
      <ul style="width:105px;margin-top:3px"><li>Financial</li><li>Healthcare</li><li>Higher Education</li></ul>
      <ul style="width:122px"><li>K12 Education</li><li>Pharmaceuticals</li><li>Public Sector - Gov't</li></ul>
      <ul><li>Retail</li><li>Sports &amp; Entertainment</li><li>Telecommunication</li><li>Transportation</li></ul>
    </div>
  </div>
  <div class="abs panel" style="left:602px;width:422px;padding-left:16px">
    <h2><b>TOP</b> SOLUTIONS</h2>
    <div class="cols">
      <ul style="width:132px"><li>BDR Solutions</li><li>Cloud Solutions</li><li>Email and Messaging</li><li>Hardware Maintenance</li></ul>
      <ul style="width:115px"><li>I.T. Security</li><li>Managed IT Support</li><li>Corvane Business</li><li>Mobility</li></ul>
      <ul><li>Solid State Technology</li><li>Unified Communication</li><li>Web Development &amp; Hosting</li></ul>
    </div>
  </div>
</section>

<footer>
  <div class="abs footer"></div>
  <h3 class="abs foot-h" style="left:207px">COMPANY INFO</h3>
  <ul class="abs foot-list" style="left:207px"><li>About Us</li><li>Advertising</li><li>Press Releases</li><li>Become an Affiliate</li></ul>
  <ul class="abs foot-list" style="left:345px"><li>FAQ</li><li>Careers</li><li>Q.R. Bright Desk solutions</li><li>Expert Soutions</li></ul>
  <h3 class="abs foot-h" style="left:515px">CUSTOMER SERVICE</h3>
  <ul class="abs foot-list" style="left:515px"><li>Help Center</li><li>Order Status</li><li>Return a Product</li><li>Low Price Guarantee</li></ul>
  <ul class="abs foot-list" style="left:663px"><li>Forgot Password?</li><li>Contact Us</li><li>Sign Up For Our Newsletter</li></ul>
  <h3 class="abs foot-h" style="left:829px">FIND US AT</h3>
  <div class="abs phone foot-phone">
    <svg width="16" height="16" viewBox="0 0 16 16"><path d="M3 1l3 3-2 2c1 2 3 4 5 5l2-2 3 3-2 3C7 14 2 9 1 3z" fill="#ccc"/></svg>888.555.0142
  </div>
  <div class="abs foot-brand"><div class="dot"></div><span>Q.R. Bright Desk</span></div>

  <div class="abs bottom"></div>
  <div class="abs legal"><span>Privacy Policy</span><span>Copyright Notice</span><span>Terms</span><span>Sitemap</span></div>
  <div class="abs social" aria-label="Social links"><i></i><i></i><i></i><i></i><i></i></div>
  <div class="abs copy">© 2013 Q.R. Bright Desk Solutions. All rights reserved</div>
</footer>

</body>
</html>
```